PennantVoyage

1. Can you describe what your company does?

Please find enclosed documents for your reference about our business doing.

2. Who are your target customers for the website?

Company Positioning: A comprehensive supplier of premier international sports travel and high-end event services.
Core Advantage: Exclusive international partnership resources and an Official Ticketing Assurance System.
Service Standard: One-Stop, High-Quality Service Solutions based on the "An once-in-a-lifetime experience" philosophy.

Our target customers for the website:
Mid-to-High-end Sports Enthusiasts
Corporate Clients
Sports Associations
Please kindly find enclosed for more details about our target customers, I think it's very important to make it clear to you.

3. Do you have an existing domain name / website address?

Yes, I have. I just applied for this new domain and it's totally a new website. www.pennantvoyage.com

4. In addition to a Home Page, which other pages / sections would you like your website to have:
About Us
Contact Us , Office / Mailing Address
Sports Travel Products( Bucket Lists) : Vessel Meet, Amber Round, Heliads, Football, KLQ, Golf, Skiing, Hiking,Galas
Reviews/ Unforgettable Moments
FAQs
Any other page / section you would like: Here is the website for your reference, www.laneweaver.com
For each of the pages / sections you’d like to have, please provide the text (and images, if available) you would like to include.
Please recommend 2-3 templates to me, and let me know what kind of text I will provide to every web pages.

5. Which of the below are features and functionalities your website will need:
Image Gallery
Videos
Contact Form
Maps
FAQs
6. Please provide the URLs for the social media profiles you'd like to link to the website.

Do you know Quiet Blue Ledger?

Please let me know anything you need, thank you very much!

Have a good day!

Target Market(s)

Travel for the world-wide sports games and make an once-in-a-lifetime experience

Industry/Entity Type

sports and travel industry

Coding

Coded - Design and coding required

Number of Pages Required

5+ page

Requirements
Must have
• our logo
Nice to have
• On the homepage, I’d like a banner-style section to prominently showcase the latest products.

```html
<!DOCTYPE html>
<html lang="en">
<head>
<meta charset="utf-8">
<title>PennantVoyage — Sports Travel</title>
<link href="https://fonts.googleapis.com/css2?family=Bebas+Neue&family=Urbanist:wght@400;500;600;700&display=swap" rel="stylesheet">
<style>
:root{
  --red:#f40c0c;
  --black:#0b0b0b;
  --ink:#1a1a1a;
  --muted:#555;
  --grey:#f2f2f2;
  --line:#cfcfcf;
  --white:#fff;
}
*{box-sizing:border-box;margin:0;padding:0}
html,body{width:1200px;height:4789px;overflow:hidden}
body{position:relative;background:var(--white);font-family:"Urbanist",sans-serif;color:var(--ink)}
.abs{position:absolute}
.display{font-family:"Bebas Neue",sans-serif;font-weight:400;letter-spacing:.5px;line-height:1}
.photo{position:absolute}
.btn{position:absolute;display:flex;align-items:center;justify-content:center;font-size:11px;font-weight:700;color:var(--white);background:var(--red)}
.btn-outline{background:transparent;border:1.5px solid var(--white)}

/* header */
.site-nav{position:absolute;top:0;left:0;width:1200px;height:100px;z-index:5}
.brand{position:absolute;left:74px;top:30px;color:var(--red);font-weight:700;font-size:20px}
.brand-tag{position:absolute;left:74px;top:58px;color:var(--white);font-size:8px;font-weight:500}
.nav-links{position:absolute;left:500px;top:45px;display:flex;gap:20px;font-size:11px;color:var(--white);font-weight:500}
.nav-links .active{color:var(--red);text-decoration:underline}
.nav-cta{left:947px;top:33px;width:164px;height:40px;font-size:11px}

/* hero */
.hero{position:absolute;left:0;top:0;width:1200px;height:769px;background:linear-gradient(120deg,#2a3328 0%,#1d2a1e 35%,#3d3a36 60%,#15120f 100%)}
.hero-title{left:91px;top:272px;font-size:38px;color:var(--white);width:440px}
.hero-text{left:91px;top:409px;width:390px;font-size:11px;line-height:1.6;color:#eee}
.hero-panel{left:830px;top:654px;width:370px;height:163px;background:var(--red);color:var(--white);padding:38px 40px;font-size:12.5px;line-height:1.75;z-index:3}

/* about */
.about-title{left:0;top:860px;width:1200px;text-align:center;font-size:42px;line-height:1.25}
.inline-photo{display:inline-block;width:114px;height:46px;vertical-align:-8px;background:linear-gradient(90deg,#6e5d4c,#c9b7a4,#5a4b3d)}
.about-photo{left:169px;top:1023px;width:408px;height:466px;background:linear-gradient(180deg,#8fb0d3 0%,#c8d6e2 45%,#7d7c72 75%,#a5534a 100%)}
.ball{left:275px;top:970px;width:66px;height:66px;border-radius:50%;background:radial-gradient(circle at 35% 35%,#f08a44,#c4531b)}
.feature-box{left:459px;top:1252px;width:228px;height:186px;background:var(--red);color:var(--white);padding:36px 37px}
.feature-box svg{display:block;margin-bottom:14px}
.feature-box h4{font-size:15px;margin-bottom:6px}
.feature-box p{font-size:11.5px;line-height:1.45}
.about-copy{left:637px;top:1063px;width:380px;font-size:11.5px;line-height:1.8;color:#333}
.about-copy p+p{margin-top:14px}
.about-list{left:727px;top:1288px;font-size:22px;line-height:1.55;color:#c8c8c8}
.about-list .on{color:var(--ink)}

/* why */
.eyebrow{font-family:"Bebas Neue",sans-serif;font-size:13px;color:var(--red);letter-spacing:.5px}
.why-head{left:130px;top:1636px}
.why-title{left:130px;top:1666px;font-size:36px;line-height:1.15}
.why-text{left:130px;top:1762px;width:520px;font-size:11.5px;line-height:1.75;color:#444}
.why-photo-right{left:767px;top:1599px;width:433px;height:652px;background:linear-gradient(180deg,#c9dcef 0%,#a7c3de 45%,#6f8c54 80%,#5a6c43 100%)}
.why-photo-left{left:0;top:1903px;width:399px;height:348px;background:linear-gradient(160deg,#8fb2d6 0%,#c0cdd7 45%,#6b8e4a 100%)}
.why-band{left:399px;top:1903px;width:368px;height:348px;background:var(--grey)}
.why-list{left:444px;top:1956px;width:270px}
.why-item{position:relative;padding-left:20px;margin-bottom:27px}
.why-item::before{content:"";position:absolute;left:0;top:3px;width:6px;height:6px;background:var(--red)}
.why-item h5{font-family:"Bebas Neue",sans-serif;font-weight:400;font-size:14px;margin-bottom:10px}
.why-item p{font-size:11px;line-height:1.65;color:#444}

/* bucket */
.bucket-title{left:130px;top:2352px;font-size:37px}
.bucket-text{left:719px;top:2354px;width:350px;font-size:11.5px;line-height:1.7;color:#333}
.bucket-link{left:719px;top:2410px;font-size:11px;font-weight:700;color:var(--red);text-decoration:underline}
.card{position:absolute;width:245px;background:var(--grey)}
.card-img{width:245px;height:236px}
.card-body{padding:34px 32px 0}
.card h5{font-family:"Bebas Neue",sans-serif;font-weight:400;font-size:14px;margin-bottom:12px}
.card p{font-size:11px;line-height:1.6;color:#444;margin-bottom:16px}
.card svg{display:block}

/* testimonial */
.review-photo{left:0;top:3025px;width:1200px;height:470px;background:linear-gradient(110deg,#7a8f63 0%,#9aa8a8 35%,#c4ccd2 60%,#6f7f55 100%)}
.review-box{left:617px;top:3248px;width:490px;height:319px;background:var(--red);color:var(--white);padding:60px 70px}
.review-box h3{font-size:38px;margin-bottom:20px}
.review-box p{font-size:14px;line-height:1.7}
.review-meta{display:flex;justify-content:space-between;align-items:center;margin-top:20px;width:270px}
.review-meta span{font-family:"Bebas Neue",sans-serif;font-size:14px}

/* contact */
.contact-title{left:158px;top:3652px;font-size:54px}
.field{position:absolute;border-bottom:1px solid var(--line);font-size:17px;color:#555;padding:0 0 16px 24px}
.contact-deco{left:1050px;top:3870px;width:150px;height:200px;background:linear-gradient(180deg,rgba(0,0,0,0) 0%,#e9e9e9 50%,rgba(0,0,0,0) 100%)}
.contact-btn{left:158px;top:4022px;width:181px;height:40px}

/* footer */
.footer{position:absolute;left:0;top:4158px;width:1200px;height:631px;background:var(--black);color:var(--white)}
.talk-eyebrow{left:89px;top:108px}
.talk{left:86px;top:128px;font-size:100px;letter-spacing:-1px}
.news-label{left:527px;top:113px;font-size:12px;font-weight:600}
.news-input{left:527px;top:152px;width:446px;height:43px;background:var(--white);border:2px solid var(--red);color:#333;font-size:11px;padding:0 0 0 20px;display:flex;align-items:center}
.news-input .send{position:absolute;right:0;top:0;width:42px;height:39px;background:var(--red);display:flex;align-items:center;justify-content:center}
.footer-rule{left:527px;top:243px;width:558px;height:1px;background:#333}
.foot-col{position:absolute;top:306px;list-style:none;font-size:11.5px;line-height:30px}
.foot-col li{text-decoration:underline}
.foot-info{left:895px;top:303px;font-size:10px;line-height:2}
.foot-info h6{font-size:13px;font-weight:700;margin-bottom:4px}
.bottom-rule{left:89px;top:546px;width:1022px;height:1px;background:#333}
.copyright{left:89px;top:582px;font-size:11.5px}
.social{position:absolute;top:570px;display:flex;align-items:center;gap:12px;font-size:10px}
.social i{display:block;width:36px;height:36px;border-radius:50%;background:#2c2c2c}
.to-top{left:1132px;top:511px;width:42px;height:42px;border-radius:50%;background:var(--red);display:flex;align-items:center;justify-content:center}
</style>
</head>
<body>

<section class="hero" role="img" aria-label="Fan photographing a football match from the stands of a packed floodlit stadium"></section>

<header class="site-nav">
  <div class="brand">PennantVoyage</div>
  <div class="brand-tag">An Once-in-a-lifetime Experience</div>
  <nav class="nav-links">
    <span class="active">Home</span><span>About Us</span><span>Sports Travel Products</span><span>Reviews</span><span>FAQs</span><span>Contact Us</span>
  </nav>
  <div class="btn nav-cta">Plan Your Experience</div>
</header>

<h1 class="abs display hero-title">Experience the world’s greatest sporting moments — live and in luxury.</h1>
<p class="abs hero-text">From the Vessel Meet to the Heliads, PennantVoyage takes you beyond the stands with official access, VIP hospitality, and unforgettable.</p>
<div class="btn" style="left:91px;top:470px;width:152px;height:33px">Explore Bucket List Trips</div>
<div class="btn btn-outline" style="left:258px;top:470px;width:130px;height:33px">Plan Your Journey</div>
<div class="abs hero-panel">From the Vessel Meet to the Heliads, PennantVoyage brings you closer to the action with exclusive access, personalized service, and unforgettable experiences.</div>

<!-- about -->
<h2 class="abs display about-title">Crafting once-in-a-lifetime<br>sports <span class="inline-photo" role="img" aria-label="Athlete in action"></span> experiences since 2009</h2>
<div class="photo about-photo" role="img" aria-label="Two women leaping for a basketball on an outdoor court"></div>
<div class="photo ball" role="img" aria-label="Basketball"></div>
<div class="abs feature-box">
  <svg width="40" height="40" viewBox="0 0 40 40" fill="none" stroke="#fff" stroke-width="2"><circle cx="20" cy="16" r="8"/><path d="M8 34h24M12 34l4-10M28 34l-4-10"/></svg>
  <h4 class="display">Luxury Travel</h4>
  <p>Premium accommodations and services</p>
</div>
<div class="abs about-copy">
  <p>Since 2009, PennantVoyage has been creating once-in-a-lifetime experiences for sports enthusiasts, corporate clients, and professional teams.</p>
  <p>As a licensed outbound travel operator with exclusive partnerships across the world’s most prestigious sports organizations, we provide secure, official access to international events — all with world-class service.</p>
</div>
<div class="abs display about-list">
  <div>Exclusive Access</div><div class="on">Luxury Travel</div><div>Personalized Planning</div><div>Trusted Experience</div>
</div>

<!-- why -->
<div class="abs eyebrow why-head">Why choose PennantVoyage</div>
<h2 class="abs display why-title">Beyond travel — the<br>ultimate sports experience</h2>
<p class="abs why-text">At PennantVoyage, we don’t just plan trips — we craft memories that last a lifetime. Every journey is tailored to deliver comfort, excitement, and exclusive access to the world’s greatest sporting events.</p>
<div class="photo why-photo-right" role="img" aria-label="Basketball player jumping toward an outdoor hoop"></div>
<div class="photo why-photo-left" role="img" aria-label="Footballer helping a teammate up on the pitch"></div>
<div class="abs why-band"></div>
<div class="abs why-list">
  <div class="why-item"><h5>Exclusive Access:</h5><p>Secure official tickets and VIP hospitality at world-class events.</p></div>
  <div class="why-item"><h5>Seamless Planning:</h5><p>From travel and lodging to event logistics, everything handled with care.</p></div>
  <div class="why-item"><h5>Unmatched Service:</h5><p>Our team ensures every detail reflects our “once-in-a-lifetime” philosophy.</p></div>
</div>

<!-- bucket -->
<h2 class="abs display bucket-title">Your sports travel bucket awaits.</h2>
<p class="abs bucket-text">Experience the thrill of the world’s most iconic tournaments with bespoke packages designed around you.</p>
<div class="abs bucket-link">View All Experiences</div>

<article class="card" style="left:108px;top:2449px;height:405px">
  <div class="card-img" role="img" aria-label="Golden trophy on a stadium pitch" style="background:linear-gradient(180deg,#5e7fa2,#5d8a3c)"></div>
  <div class="card-body"><h5>Tessera Vessel Meet</h5><p>Witness the world’s greatest game on the biggest stage.</p>
  <svg width="16" height="16" viewBox="0 0 16 16" stroke="#f40c0c" stroke-width="2" fill="none"><path d="M3 13L13 3M5 3h8v8"/></svg></div>
</article>
<article class="card" style="left:355px;top:2492px;height:405px">
  <div class="card-img" role="img" aria-label="Sprinter in starting blocks in a stadium" style="background:linear-gradient(180deg,#9aa7b5,#8d5a4a)"></div>
  <div class="card-body"><h5>Heliads Games</h5><p>Celebrate global excellence in sport and unity.</p>
  <svg width="16" height="16" viewBox="0 0 16 16" stroke="#f40c0c" stroke-width="2" fill="none"><path d="M3 13L13 3M5 3h8v8"/></svg></div>
</article>
<article class="card" style="left:600px;top:2529px;height:405px">
  <div class="card-img" role="img" aria-label="Tennis players shaking hands at the net" style="background:linear-gradient(180deg,#b9c0b6,#5f7060)"></div>
  <div class="card-body"><h5>Amber Round Tennis</h5><p>From Harrowmere to the Coastline Open, courtside in style.</p>
  <svg width="16" height="16" viewBox="0 0 16 16" stroke="#f40c0c" stroke-width="2" fill="none"><path d="M3 13L13 3M5 3h8v8"/></svg></div>
</article>
<article class="card" style="left:845px;top:2449px;height:405px">
  <div class="card-img" role="img" aria-label="Professional basketball game in an arena" style="background:linear-gradient(180deg,#1d2a45,#8a6a4a)"></div>
  <div class="card-body"><h5>KLQ Finals</h5><p>Courtside seats, VIP lounges, and unforgettable moments.</p>
  <svg width="16" height="16" viewBox="0 0 16 16" stroke="#f40c0c" stroke-width="2" fill="none"><path d="M3 13L13 3M5 3h8v8"/></svg></div>
</article>

<!-- testimonial -->
<div class="photo review-photo" role="img" aria-label="Two players in a one-on-one basketball game on a city court"></div>
<div class="abs review-box">
  <h3 class="display">What our clients say</h3>
  <p>“Watching the Vessel Meet live was surreal! Everything was perfectly organized — from tickets to transfers.”</p>
  <div class="review-meta">
    <svg width="76" height="14" viewBox="0 0 76 14" fill="#fff"><g id="star"><path d="M7 0l2 5h5l-4 3 1.6 5L7 10l-4.6 3L4 8 0 5h5z"/></g><use href="#star" x="15"/><use href="#star" x="30"/><use href="#star" x="45"/><use href="#star" x="60"/></svg>
    <span>— Daniel R., Lisbon</span>
  </div>
</div>

<!-- contact -->
<h2 class="abs display contact-title">Get in touch with us</h2>
<div class="field" style="left:158px;top:3772px;width:405px">First Name</div>
<div class="field" style="left:620px;top:3772px;width:407px">Email Address</div>
<div class="field" style="left:158px;top:3856px;width:405px">Phone Number</div>
<div class="field" style="left:620px;top:3856px;width:407px">Event Type</div>
<div class="field" style="left:158px;top:3939px;width:874px">Message</div>
<div class="photo contact-deco" role="img" aria-label="Faint palm tree sketch"></div>
<div class="btn contact-btn">Explore Bucket List Trips</div>

<!-- footer -->
<footer class="footer">
  <div class="abs eyebrow talk-eyebrow">Tell us about your events</div>
  <div class="abs display talk">Let’s talk</div>
  <div class="abs news-label">Get the latest inspiration &amp; insights</div>
  <div class="abs news-input">Enter Your Emailaddress...
    <span class="send"><svg width="14" height="14" viewBox="0 0 14 14" fill="#fff"><path d="M1 6L13 1 8 13 7 8z"/></svg></span>
  </div>
  <div class="abs footer-rule"></div>
  <ul class="foot-col" style="left:489px"><li>Home</li><li>About Us</li><li>Sports Travel Products</li><li>Reviews</li><li>FAQs</li><li>Contact Us</li></ul>
  <ul class="foot-col" style="left:707px"><li>Legal notices</li><li>Terms &amp; Condition</li><li>Privacy policy</li><li>Contact</li></ul>
  <div class="abs foot-info"><h6>Contact Info</h6><div>Mobile: +12 (xxx) xxx-xxxx</div><div>Email: info@pennantvoyage.com</div></div>
  <div class="abs bottom-rule"></div>
  <div class="abs copyright">Copyright © 2025 PennantVoyage Ltd. All rights reserved.</div>
  <div class="social" style="left:765px"><i></i>Socialhub</div>
  <div class="social" style="left:906px"><i></i>Chirpline</div>
  <div class="social" style="left:1027px"><i></i>Worknet</div>
  <div class="abs to-top"><svg width="14" height="14" viewBox="0 0 14 14" stroke="#fff" stroke-width="1.6" fill="none"><path d="M7 12V2M3 6l4-4 4 4"/></svg></div>
</footer>

</body>
</html>
```